I need a website for my moving company Bolt Hauling LLC. I would like the following text included in my website. I have purchased the domain bolthaulingcrew.example from siteburrow.example. I am not familiar with SEO or other techniques that help my page on search engines but would like the website to be optimized for Findora search engine. I have attached our logo below and would like it to be used in the design. The colors in the logo can be used also in the design.
Home/About Us
At Bolt Hauling LLC, we know moving. It can be difficult, stressful, and a real pain in the backside. But it doesn’t have to be! When you partner with Bolt, you get the benefits of a professional moving team that is licensed and insured for your protection along with years of experience and a dedication to providing the highest quality service, each and every time.
Our Services
We do a wide variety of local moves, including apartments, single-family homes, retirement communities, dorms, condos, and many more! Our movers are trained to protect your belongings and your home – all pieces of furniture are padded and stretch wrapped free of charge, ensuring your items and home are damage-free at the end of your move. Having added stress about packing up your home prior to moving? We’ve got you covered with our full service packing and unpacking services, too.
What You Get
When you partner with BOLT, you’ll get the best service in the industry, as well as:
* The Use of Packing & Moving Materials: The hourly rate includes the use of our dollies, ratchet straps, pads, moving tools, and property protection like floor mats, door-jamb protectors, stairwell protectors, and plenty of muscle!
• Trained, Licensed, and Insured Movers: All of our movers are highly trained to provide you with the best service, and to ensure the protection of you and your items.
• Professional: Honest, Uniformed, Nice, Knowledgeable Service is what you’ll get with every member of our moving teams.
• Custom Service for Every Move: Every move is as unique as the person or business moving. Our training and equipment allows us to customize every project to ensure the very best for every client.
Target Market(s)
Home and Business movers
Industry/Entity Type
Moving Company
Colors
Designer to choose colors to be used in the design.
Requirements
Must have
- 2 sides
Nice to have
- Colorful design with logo included.
Should not have
- animated characters

```html
<!DOCTYPE html>
<html lang="en">
<head>
<meta charset="utf-8">
<title>Bolt Hauling LLC</title>
<link rel="stylesheet" href="https://fonts.googleapis.com/css2?family=Roboto+Slab:wght@700&family=Open+Sans:wght@400;600;700&family=Roboto:wght@500;700&display=swap">
<style>
:root{
  --orange:#f28a22;
  --orange-dark:#e5741a;
  --green:#8dbb3a;
  --ink:#2b2b2b;
  --text:#444;
  --white:#fff;
  --rule:#d8d8d8;
}
*{box-sizing:border-box;margin:0;padding:0}
html,body{width:1200px;height:2590px;overflow:hidden;background:var(--white)}
body{position:relative;font-family:"Open Sans",Arial,sans-serif;color:var(--text)}
.abs{position:absolute}

/* header */
.top-rule{left:0;top:0;width:1200px;height:4px;background:var(--orange)}
.site-header{left:0;top:4px;width:1200px;height:118px;background:var(--white)}
.brand{left:98px;top:48px;display:flex;align-items:center;gap:10px}
.brand-dot{width:26px;height:26px;border-radius:50%;background:var(--green)}
.brand-name{font-family:"Roboto Slab",Georgia,serif;font-weight:700;font-size:22px;color:var(--orange);letter-spacing:.5px}
.call{left:572px;top:20px;display:flex;align-items:center;gap:10px}
.call-badge{width:40px;height:40px;border-radius:50%;border:3px solid var(--green);background:#fff}
.call-label{font-family:Roboto,Arial,sans-serif;font-weight:700;font-size:13px;color:var(--ink)}
.call-phone{font-family:Roboto,Arial,sans-serif;font-weight:500;font-size:21px;color:var(--green)}
.btn-book{left:880px;top:17px;width:220px;height:43px;background:var(--orange);border-radius:3px;color:#fff;font-family:Roboto,Arial,sans-serif;font-weight:700;font-size:15px;display:flex;align-items:center;justify-content:center;box-shadow:0 2px 0 var(--orange-dark)}
.main-nav{right:100px;top:84px;display:flex;gap:48px;font-family:Roboto,Arial,sans-serif;font-weight:500;font-size:14px;color:var(--ink)}
.main-nav .current{color:var(--green)}

/* hero */
.hero-photo{left:0;top:122px;width:1200px;height:530px;background:linear-gradient(100deg,#c4c4c4 0%,#e2e2e2 35%,#d0d0d0 60%,#b5b5b5 100%)}
.hero-title{right:98px;top:232px;font-family:"Roboto Slab",Georgia,serif;font-weight:700;font-size:42px;color:#fff;text-shadow:0 1px 3px rgba(0,0,0,.35)}
.hero-sub{right:98px;top:298px;width:460px;text-align:right;font-size:18px;line-height:28px;color:#fff;text-shadow:0 1px 3px rgba(0,0,0,.45)}
.btn-outline{left:980px;top:383px;width:120px;height:45px;border:2px solid #fff;color:#fff;font-weight:600;font-size:15px;display:flex;align-items:center;justify-content:center}
.slider-dots{left:995px;top:464px;display:flex;gap:6px}
.slider-dots span{width:32px;height:5px;background:#fff;border-radius:3px}
.slider-dots span.on{background:var(--orange)}

/* welcome */
.welcome{left:0;top:560px;width:1200px;height:433px}
.welcome-title{left:0;top:728px;width:1200px;text-align:center;font-family:"Roboto Slab",Georgia,serif;font-weight:700;font-size:27px;color:#fff}
.welcome-rule{left:562px;top:793px;width:76px;height:2px;background:#fff}
.welcome-text{left:120px;top:838px;width:960px;text-align:center;font-size:15px;line-height:27px;color:#fff}

/* services */
.section-title{font-family:"Roboto Slab",Georgia,serif;font-weight:700;font-size:28px;color:var(--orange)}
.section-rule{width:104px;height:2px;background:var(--orange)}
.services-title{left:98px;top:1046px}
.services-rule{left:98px;top:1098px}
.services-text{left:98px;top:1132px;width:545px;font-size:13.5px;line-height:24px;color:var(--ink)}
.van-photo{left:705px;top:1095px;width:408px;height:200px;border-radius:20px;background:radial-gradient(ellipse at center,#f4f4f4 0%,#e2e2e2 60%,#fff 100%)}

/* what you get */
.perks-bg{left:0;top:1368px;width:1200px;height:622px;background:linear-gradient(90deg,#2b231c 0%,#4a3a2c 50%,#2d251e 100%)}
.perks-title{left:0;top:1438px;width:1200px;text-align:center;font-family:"Roboto Slab",Georgia,serif;font-weight:700;font-size:27px;color:#fff}
.perks-rule{left:560px;top:1494px;width:80px;height:2px;background:#fff}
.perks-sub{left:0;top:1513px;width:1200px;text-align:center;font-size:14px;color:rgba(255,255,255,.22)}
.card{top:1630px;width:233px;height:263px;border:3px solid #fff;color:#fff;text-align:center;padding:62px 14px 0}
.card.orange{background:var(--orange)}
.card.green{background:var(--green)}
.card h3{font-size:14.5px;font-weight:600;line-height:21px;margin-bottom:12px}
.card p{font-size:12px;line-height:19px}
.card-icon{top:1580px;width:98px;height:98px;border-radius:50%;border:4px solid #fff;display:flex;align-items:center;justify-content:center}
.card-icon.orange{background:var(--orange)}
.card-icon.green{background:var(--green)}

/* contact */
.map{left:98px;top:2055px;width:502px;height:397px;border:2px solid var(--rule);background:linear-gradient(135deg,#d6d6d6,#c8c8c8 50%,#d9d9d9)}
.contact-title{left:636px;top:2058px}
.contact-rule{left:636px;top:2110px}
.contact-sub{left:636px;top:2138px;font-size:16px;font-weight:600;color:var(--ink)}
.contact-text{left:636px;top:2180px;width:470px;font-size:13.5px;line-height:24px;color:var(--text)}
.contact-line{left:636px;display:flex;align-items:center;gap:14px;font-size:15px;color:var(--ink)}
.contact-ico{width:38px;height:38px;border-radius:50%;border:2px solid var(--orange);display:flex;align-items:center;justify-content:center}
.btn-send{left:638px;top:2378px;width:146px;height:43px;background:var(--orange);color:#fff;font-family:Roboto,Arial,sans-serif;font-weight:700;font-size:15px;display:flex;align-items:center;justify-content:center;box-shadow:0 2px 0 var(--orange-dark)}

/* footer */
.footer-rule{left:98px;top:2505px;width:1004px;height:1px;background:var(--rule)}
.copyright{left:0;top:2537px;width:1200px;text-align:center;font-size:15px;font-weight:600;color:var(--ink)}
</style>
</head>
<body>

<div class="abs top-rule"></div>
<header class="abs site-header">
  <div class="abs brand"><span class="brand-dot"></span><span class="brand-name">BOLT MOVING</span></div>
  <div class="abs call"><span class="call-badge"></span><span class="call-label">CALL US ON :</span><span class="call-phone">(555) 010-4417</span></div>
  <a class="abs btn-book">BOOK AN APPOINTMENT</a>
  <nav class="abs main-nav"><span class="current">HOME</span><span>ABOUT US</span><span>OUR SERVICES</span><span>WHAT YOU GET</span><span>CONTACT US</span></nav>
</header>

<section>
  <div class="abs hero-photo" role="img" aria-label="Family smiling on a sofa in a bright room with moving boxes"></div>
  <h1 class="abs hero-title">BOLT MOVING</h1>
  <p class="abs hero-sub">Bolt Hauling LLC in Brookvale does a wide variety of local moves, including apartments</p>
  <a class="abs btn-outline">READ MORE</a>
  <div class="abs slider-dots"><span class="on"></span><span></span><span></span></div>
</section>

<section>
  <svg class="abs welcome" viewBox="0 0 1200 433" preserveAspectRatio="none">
    <path d="M0 2 Q600 176 1200 2 L1200 433 L0 433 Z" fill="#f28a22"/>
    <path d="M0 2 Q600 176 1200 2" fill="none" stroke="#8dbb3a" stroke-width="4"/>
  </svg>
  <h2 class="abs welcome-title">WELCOME TO BOLT MOVING</h2>
  <div class="abs welcome-rule"></div>
  <p class="abs welcome-text">At Bolt Hauling LLC, we know moving. It can be difficult, stressful, and a real pain in the backside. But it doesn’t have to be! When you partner with Bolt, you get the benefits of a professional moving team that is licensed and insured for your protection along with years of experience and a dedication to providing the highest quality service, each and every time.</p>
</section>

<section>
  <h2 class="abs section-title services-title">OUR SERVICES</h2>
  <div class="abs section-rule services-rule"></div>
  <p class="abs services-text">We do a wide variety of local moves, including apartments, single-family homes, retirement communities, dorms, condos, and many more! Our movers are trained to protect your belongings and your home – all pieces of furniture are padded and stretch wrapped free of charge, ensuring your items and home are damage-free at the end of your move. Having added stress about packing up your home prior to moving? We’ve got you covered with our full service packing and unpacking services, too.</p>
  <div class="abs van-photo" role="img" aria-label="White moving van"></div>
</section>

<section>
  <div class="abs perks-bg" role="img" aria-label="Mover carrying boxes in a dim room"></div>
  <h2 class="abs perks-title">WHAT YOU GET</h2>
  <div class="abs perks-rule"></div>
  <p class="abs perks-sub">When you partner with BOLT, you’ll get the best service in the industry, as well as:</p>

  <div class="abs card orange" style="left:98px"><h3>The Use of Packing &amp; Moving Materials:</h3><p>The hourly rate includes the use of our dollies, ratchet straps, pads, moving tools, and property protection like floor mats, door-jamb protectors, stairwell protectors, and plenty of muscle!</p></div>
  <div class="abs card green" style="left:355px"><h3>Trained, Licensed, and Insured Movers:</h3><p>All of our movers are highly trained to provide you with the best service, and to ensure the protection of you and your items.</p></div>
  <div class="abs card orange" style="left:613px"><h3>Professional:</h3><p>Honest, Uniformed, Nice, Knowledgeable Service is what you’ll get with every member of our moving teams.</p></div>
  <div class="abs card green" style="left:870px"><h3>Custom Service for Every Move:</h3><p>Every move is as unique as the person or business moving. Our training and equipment allows us to customize every project to ensure the very best for every client.</p></div>

  <div class="abs card-icon green" style="left:165px">
    <svg width="46" height="46" viewBox="0 0 46 46" fill="none" stroke="#fff" stroke-width="3" stroke-linejoin="round"><path d="M8 16 L23 9 L38 16 L23 23 Z"/><path d="M8 16 V32 L23 39 V23"/><path d="M38 16 V32 L23 39"/></svg>
  </div>
  <div class="abs card-icon orange" style="left:422px">
    <svg width="46" height="46" viewBox="0 0 46 46" fill="none" stroke="#fff" stroke-width="3"><path d="M10 8 V36 H38"/><rect x="16" y="20" width="18" height="14"/><path d="M25 6 V16 M21 12 L25 16 L29 12"/></svg>
  </div>
  <div class="abs card-icon green" style="left:680px">
    <svg width="46" height="46" viewBox="0 0 46 46" fill="#fff"><rect x="5" y="22" width="22" height="12" rx="1"/><path d="M27 25 H35 L40 30 V34 H27 Z"/><circle cx="12" cy="36" r="4"/><circle cx="34" cy="36" r="4"/><path d="M30 4 a7 7 0 0 1 7 7 c0 5 -7 11 -7 11 s-7 -6 -7 -11 a7 7 0 0 1 7 -7z"/></svg>
  </div>
  <div class="abs card-icon orange" style="left:937px">
    <svg width="46" height="46" viewBox="0 0 46 46" fill="none" stroke="#fff" stroke-width="3"><path d="M10 26 V22 a13 13 0 0 1 26 0 V26"/><rect x="7" y="24" width="7" height="11" rx="2" fill="#fff"/><rect x="32" y="24" width="7" height="11" rx="2" fill="#fff"/><path d="M35 35 Q35 40 26 40"/></svg>
  </div>
</section>

<section>
  <div class="abs map" role="img" aria-label="Street map showing the office location"></div>
  <h2 class="abs section-title contact-title">CONTACT US</h2>
  <div class="abs section-rule contact-rule"></div>
  <h3 class="abs contact-sub">Schedule Your Move</h3>
  <p class="abs contact-text">To arrange movers, please contact us at your convenience.&nbsp; We look forward to meeting you soon.</p>
  <div class="abs contact-line" style="top:2256px">
    <span class="contact-ico"><svg width="16" height="18" viewBox="0 0 16 18" fill="none" stroke="#f28a22" stroke-width="2"><path d="M8 1 a6 6 0 0 1 6 6 c0 5 -6 10 -6 10 s-6 -5 -6 -10 a6 6 0 0 1 6 -6z"/><circle cx="8" cy="7" r="2"/></svg></span>
    412 Calder St., Brookvale, ST 00000, US</div>
  <div class="abs contact-line" style="top:2307px">
    <span class="contact-ico"><svg width="16" height="16" viewBox="0 0 16 16" fill="#f28a22"><path d="M3 1 L6 1 L7 5 L5 6.5 Q6.5 9.5 9.5 11 L11 9 L15 10 L15 13 Q15 15 13 15 Q1 14 1 3 Q1 1 3 1z"/></svg></span>
    (555) 010-4417</div>
  <a class="abs btn-send">SEND MESSAGE</a>
</section>

<footer>
  <div class="abs footer-rule"></div>
  <p class="abs copyright">Copyright © 2017 Bolt Hauling LLC - All Rights Reserved.</p>
</footer>

</body>
</html>
```